A Produce Business Needs a Website Graphic

The name of our company is 'K.T. Wellsford Co., Inc.' Located in the Bronx, NY, we are a wholesale produce distributor asking you to create a graphic for our new website. The design needs to showcase our core values: QService, Satisfaction, and Integrity. Our logo colors are lime green and blue, so we would like to see graphics that incorporate similar tones. The final design should communicate our desire to serve our customers with the values mentioned above. (For your convenience, we have attached our logo to this brief.)

Target Market(s)

Potential/Current Customers & Shippers

Industry/Entity Type

Business

Font styles to use
Other font styles liked:
• Your Choice

Colors
acd036
9bcb3c
33a6d7
0892cd
0355a3
3176b5
fbf289
fbee3d

Requirements
Must have
• Showcase core values: Quality Service, Satisfaction, and Integrity
Nice to have
• Fruit/Veg incorporated in the design

```html
<!DOCTYPE html>
<html lang="en">
<head>
<meta charset="UTF-8">
<title>K.T. Wellsford – Core Values</title>
<link href="https://fonts.googleapis.com/css2?family=Montserrat:wght@500;600&display=swap" rel="stylesheet">
<style>
  :root {
    --brand-blue: #1559a8;
    --brand-green: #9bcb3c;
    --veil: rgba(255, 255, 255, 0.72);
    --pill-veil: rgba(255, 255, 255, 0.62);
    --tomato: #c4301f;
    --tomato-dark: #6e1510;
    --leaf: #6f9a55;
    --leaf-dark: #2f4d36;
    --carrot: #d9663a;
  }
  * { margin: 0; padding: 0; box-sizing: border-box; }
  html, body { width: 1200px; height: 873px; overflow: hidden; background: #fff; }
  .banner {
    position: relative;
    width: 1200px;
    height: 873px;
    overflow: hidden;
    font-family: "Montserrat", sans-serif;
  }
  .produce-photo {
    position: absolute;
    inset: 0;
    background:
      radial-gradient(ellipse 420px 320px at 1060px 330px, var(--carrot) 0%, rgba(217,102,58,0) 70%),
      radial-gradient(ellipse 520px 300px at 820px 120px, var(--leaf-dark) 0%, rgba(47,77,54,0) 75%),
      radial-gradient(ellipse 500px 260px at 560px 320px, #a8c48c 0%, rgba(168,196,140,0) 75%),
      radial-gradient(ellipse 760px 520px at 260px 700px, var(--tomato) 0%, rgba(196,48,31,0) 80%),
      radial-gradient(ellipse 600px 400px at 700px 760px, #d4553e 0%, rgba(212,85,62,0) 80%),
      linear-gradient(180deg, #8fae7a 0%, #9a5a3c 45%, var(--tomato-dark) 100%);
  }
  .corner-veil {
    position: absolute;
    left: 0;
    top: 0;
  }
  .brand {
    position: absolute;
    left: 70px;
    top: 118px;
    display: flex;
    align-items: center;
    gap: 14px;
  }
  .brand-dot {
    width: 26px;
    height: 26px;
    border-radius: 50%;
    background: var(--brand-green);
  }
  .brand-name {
    font-weight: 600;
    font-size: 50px;
    color: var(--brand-blue);
    letter-spacing: 0.5px;
  }
  .brand-tagline {
    position: absolute;
    left: 164px;
    top: 212px;
    font-size: 15px;
    font-weight: 500;
    color: var(--brand-blue);
  }
  .value-pill {
    position: absolute;
    right: -60px;
    height: 140px;
    border: 3px solid var(--brand-green);
    border-radius: 70px 0 0 70px;
    background: var(--pill-veil);
    display: flex;
    align-items: center;
    font-size: 55px;
    font-weight: 500;
    color: var(--brand-blue);
  }
  .value-quality { left: 598px; top: 415px; padding-left: 68px; }
  .value-satisfaction { left: 655px; top: 567px; padding-left: 102px; }
  .value-integrity { left: 709px; top: 720px; padding-left: 130px; }
</style>
</head>
<body>
  <div class="banner">
    <div class="produce-photo" role="img" aria-label="Close-up photo of fresh red tomatoes in front, with carrots and leafy green vegetables blurred behind"></div>

    <svg class="corner-veil" width="1200" height="873" viewBox="0 0 1200 873" aria-hidden="true">
      <path d="M0,0 H830 C770,170 590,330 0,372 Z" fill="var(--veil)"/>
      <path d="M830,0 C770,170 590,330 0,372" fill="none" stroke="var(--brand-green)" stroke-width="3"/>
    </svg>

    <div class="brand">
      <span class="brand-dot"></span>
      <span class="brand-name">K.T. Wellsford</span>
    </div>
    <p class="brand-tagline">Fruits, Produce &amp; Tropicals</p>

    <div class="value-pill value-quality">Quality Service</div>
    <div class="value-pill value-satisfaction">Satisfaction</div>
    <div class="value-pill value-integrity">Integrity</div>
  </div>
</body>
</html>
```